looking for sleek business card to standout from the crowd!

We are a young biotechnology company looking to help you personalize your health through understanding your genetic make up. We need you help in making a clean but sleek business card design using our new logo. The goal? Any time we give our cards out, people say "nice card!" The feel we are going for is "modern-techy". We don't want to come across as an old, giant pharma company, but not trying to be a hipster either.

Target Market(s)

healthcare and biotechnology industry.

Industry/Entity Type

Biotechnology

Contact Information for Business Card

Info to include on the card will be NAME, TITLE, EMAIL, PHONE. The companies website (www.morvalytics.com) should also be on the card some where. Would like the logo, when printed, to be raised.

Requirements
Must have
• The logo we have attached in the color it is in. Fonts for text should lean toward more professional/tech.
Nice to have
• Prefer white/light color background
Should not have
• cartoons, landscape backgrounds images.

```html
<!DOCTYPE html>
<html lang="en">
<head>
<meta charset="utf-8">
<title>Morvalytics Business Card</title>
<link href="https://fonts.googleapis.com/css2?family=Arimo:wght@400;700&display=swap" rel="stylesheet">
<style>
  :root {
    --backdrop: #3b3431;
    --card: #141516;
    --brand-blue: #2e6da8;
    --accent-blue: #2f86d1;
    --brand-green: #7dc242;
    --text-light: #e4e6e8;
    --text-muted: #8a8d91;
    --divider: #55585c;
  }
  * { margin: 0; padding: 0; box-sizing: border-box; }
  html, body {
    width: 1200px; height: 864px; overflow: hidden;
    background: var(--backdrop);
    font-family: "Arimo", Arial, sans-serif;
  }
  .canvas {
    position: relative; width: 1200px; height: 864px;
  }
  .card {
    position: absolute;
    width: 525px; height: 300px;
    background: var(--card);
    border-radius: 4px;
    box-shadow: 0 14px 30px rgba(0,0,0,0.45);
  }
  .card-front { left: 50px; top: 282px; }
  .card-back  { left: 625px; top: 282px; }

  .front-brand {
    position: absolute; left: 70px; top: 100px;
    display: flex; align-items: center; gap: 14px;
  }
  .brand-name {
    font-weight: 700; font-size: 40px; letter-spacing: 1px;
    color: var(--brand-blue);
  }
  .brand-dot {
    width: 50px; height: 50px; border-radius: 50%;
    background: var(--brand-green);
  }
  .front-url {
    position: absolute; left: 72px; top: 190px;
    font-size: 13px; letter-spacing: 4px; color: var(--text-muted);
  }

  .back-brand {
    position: absolute; left: 40px; top: 0; bottom: 0; width: 170px;
    display: flex; flex-direction: column; align-items: center; justify-content: center; gap: 12px;
  }
  .back-brand .brand-dot { width: 96px; height: 96px; }
  .back-brand .brand-name { font-size: 17px; color: var(--brand-green); letter-spacing: 1px; }
  .divider {
    position: absolute; left: 232px; top: 70px; width: 1px; height: 160px;
    background: var(--divider);
  }
  .contact {
    position: absolute; left: 256px; top: 82px;
  }
  .person-name { font-size: 19px; font-weight: 700; color: var(--accent-blue); }
  .person-title { font-size: 15px; color: var(--brand-green); margin-top: 2px; margin-bottom: 12px; }
  .contact-row {
    display: flex; align-items: center; gap: 10px;
    font-size: 14px; color: var(--text-light); margin-top: 6px;
  }
  .contact-row svg { width: 14px; height: 14px; fill: var(--accent-blue); flex: none; }
</style>
</head>
<body>
<main class="canvas">
  <section class="card card-front">
    <div class="front-brand">
      <span class="brand-name">MORVALYTICS</span>
      <span class="brand-dot"></span>
    </div>
    <p class="front-url">www.morvalytics.com</p>
  </section>

  <section class="card card-back">
    <div class="back-brand">
      <span class="brand-dot"></span>
      <span class="brand-name">MORVALYTICS</span>
    </div>
    <div class="divider"></div>
    <div class="contact">
      <p class="person-name">Elan Marsh</p>
      <p class="person-title">President</p>
      <p class="contact-row">
        <svg viewBox="0 0 16 16" aria-hidden="true"><path d="M3 1h3l1.5 4-2 1.3a9 9 0 0 0 4.2 4.2L11 8.5l4 1.5v3a2 2 0 0 1-2 2A13 13 0 0 1 1 3a2 2 0 0 1 2-2z"/></svg>
        <span>555 0142 7781</span>
      </p>
      <p class="contact-row">
        <svg viewBox="0 0 16 16" aria-hidden="true"><path d="M1 3h14v10H1z M1 3l7 6 7-6" stroke="#141516" stroke-width="1.2"/></svg>
        <span>emarsh@morvalytics.com</span>
      </p>
      <p class="contact-row">
        <svg viewBox="0 0 16 16" aria-hidden="true"><circle cx="8" cy="8" r="7"/><path d="M1 8h14M8 1c3 3 3 11 0 14M8 1c-3 3-3 11 0 14" stroke="#141516" stroke-width="1" fill="none"/></svg>
        <span>www.morvalytics.com</span>
      </p>
    </div>
  </section>
</main>
</body>
</html>
```